To revamp the exting web page and Company presentation to new propsective client

We are company establish in 2006. We have a combine of Veltra implementation team of more than 10 years. We focus on the following areas

a) Veltra Nimbus suite implementation
b) Veltra Nimbus suite platform migration
c) Large database size in excess of 20TB

We need to redesign a our existing new card to give a new look and refresh look. Kindly visit our website for more info www.halvtek.com

Your main them is blue color and hope to hear from you all.

Target Market(s)

Professional clients

Industry/Entity Type

Information Technology

Contact Information for Business Card

To market our as the leading Veltra partner in Veltra nimbus suite implementation

Number of Pages Required

1 page

Colors
3276b5
9bcb3c
cadf82
33a6d7

Requirements
Must have
• The ability to attract new customer and show a level of professionalism.
• You can also add a green color to represent green and environmental friendly.
Nice to have
• To give a total new fresh look for the company
Should not have
• None

```html
<!DOCTYPE html>
<html lang="en">
<head>
<meta charset="utf-8">
<title>Halvtek Systems – Business Card</title>
<link rel="stylesheet" href="https://fonts.googleapis.com/css2?family=Open+Sans:wght@400;600;700&display=swap">
<style>
  :root {
    --page-bg: #e6e7ea;
    --card-white: #ffffff;
    --navy: #2a2d78;
    --navy-deep: #1b2566;
    --blue: #3276b5;
    --blue-mid: #3d6ea8;
    --blue-dark: #2a4f8c;
    --text-grey: #4a4f63;
    --sky: #33a6d7;
  }
  * { box-sizing: border-box; margin: 0; padding: 0; }
  html, body {
    width: 1200px; height: 1200px; overflow: hidden;
    background: var(--page-bg);
    font-family: "Open Sans", Arial, sans-serif;
  }
  .card {
    position: absolute; left: 160px;
    width: 880px; height: 528px;
    overflow: hidden;
    box-shadow: 0 6px 18px rgba(0,0,0,0.18);
  }
  /* Front */
  .card--front { top: 40px; background: var(--card-white); }
  .contact {
    position: absolute; right: 64px; top: 40px;
    text-align: right; color: var(--text-grey);
    font-size: 17px; line-height: 1.55;
  }
  .contact__name {
    color: var(--navy); font-size: 30px; font-weight: 700;
    letter-spacing: 0.5px; line-height: 1.2;
  }
  .contact__title { font-size: 16px; margin-bottom: 6px; }
  .contact__label { color: var(--navy); font-weight: 600; }
  .brand {
    position: absolute; right: 64px; top: 292px;
    text-align: right; color: var(--navy);
  }
  .brand__row { display: flex; align-items: center; justify-content: flex-end; gap: 14px; }
  .brand__dot { width: 22px; height: 22px; border-radius: 50%; background: var(--navy); }
  .brand__name { font-size: 46px; font-weight: 700; letter-spacing: 8px; line-height: 1; }
  .brand__sub { font-size: 11px; letter-spacing: 4px; margin-top: 4px; }
  .brand__web { font-size: 15px; letter-spacing: 5px; margin-top: 6px; }
  .band { position: absolute; left: 0; bottom: 0; width: 880px; height: 240px; }
  .decor--front {
    position: absolute; left: 40px; top: 230px; width: 420px; height: 270px;
    border-radius: 120px 140px 60px 90px;
    background: radial-gradient(ellipse at 50% 55%, #26306f 0%, #2c3a80 55%, rgba(50,80,150,0) 100%);
  }
  /* Back */
  .card--back {
    top: 632px;
    background: linear-gradient(160deg, var(--blue) 0%, var(--blue-dark) 45%, var(--navy-deep) 100%);
    color: #ffffff;
  }
  .back-brand { position: absolute; left: 60px; top: 74px; }
  .back-brand__name { font-size: 66px; font-weight: 700; letter-spacing: 14px; line-height: 1; }
  .back-brand__sub { font-size: 12px; letter-spacing: 5px; margin-top: 8px; }
  .address {
    position: absolute; right: 56px; top: 96px;
    text-align: right; font-size: 18px; line-height: 1.6;
  }
  .decor--back {
    position: absolute; left: 150px; top: 250px; width: 470px; height: 250px;
    border-radius: 130px 150px 70px 100px;
    background: radial-gradient(ellipse at 50% 55%, #141b52 0%, #1d2866 55%, rgba(30,40,100,0) 100%);
  }
</style>
</head>
<body>
  <section class="card card--front">
    <svg class="band" viewBox="0 0 880 240" aria-hidden="true">
      <defs>
        <linearGradient id="bandFill" x1="0" y1="0" x2="0" y2="1">
          <stop offset="0" stop-color="#4a7fb8"/>
          <stop offset="1" stop-color="#2d5a97"/>
        </linearGradient>
      </defs>
      <path d="M0 40 C120 10 220 70 330 60 C460 48 560 110 880 90 L880 240 L0 240 Z" fill="url(#bandFill)"/>
    </svg>
    <div class="decor--front" role="img" aria-label="Abstract pixelated molecule graphic in navy and blue"></div>

    <div class="contact">
      <div class="contact__name">DANIEL KOH</div>
      <div class="contact__title">Chief Operating Officer</div>
      <div><span class="contact__label">M:</span> 60 12 555 0142</div>
      <div><span class="contact__label">T:</span> 603 - 5550 1280</div>
      <div><span class="contact__label">E:</span> danielkoh@halvtek.com</div>
      <div><span class="contact__label">F:</span> 603 - 5550 1281</div>
      <div>65 5550 3371 (Singapore)</div>
    </div>

    <div class="brand">
      <div class="brand__row">
        <span class="brand__dot"></span>
        <span class="brand__name">HALVTEK</span>
      </div>
      <div class="brand__sub">Systems Sdn Bhd</div>
      <div class="brand__web">www.halvtek.com</div>
    </div>
  </section>

  <section class="card card--back">
    <div class="back-brand">
      <div class="back-brand__name">HALVTEK</div>
      <div class="back-brand__sub">Systems Sdn Bhd</div>
    </div>
    <div class="address">
      <div>Suite 4.02, 4th Floor</div>
      <div>Wisma Arjuna, Jalan Seri Teratai</div>
      <div>50450 Kuala Lumpur, Malaysia</div>
    </div>
    <div class="decor--back" role="img" aria-label="Abstract pixelated molecule graphic in dark navy"></div>
  </section>
</body>
</html>
```